Slatebook App Analytics Dashboard Design

Our app is designed for visitors centers and hotel/lodging concierges to assist (and allow) travelers to book tours and activities on-site with a kiosk or at front desk. This analytics dashboard will help the hotels or visitors centers owners and employees to understand the activity within their app for their specific business.

We would like this to be modern, clean and sleek and really stand out when we highlight it at an upcoming presentation/conference. The stats we would like to show are:
(By day/month/time period)
Number of Bookings
Source of Bookings i.e. website vs mobile vs kiosk (% of a whole)
Top 5 tour operators booked (and volume of each)
Top 5 tours booked (and volume of each)
Commissions earned (*admin only option - won't show for regular users)

I am including some screen shots of our current Slatebook app to see our general design and color palate. We would like to use this library: https://quillarch.com/open-source/meridian/gallery

This could lead to further UX design improvements for our current app and future projects. I will be paying out a winner and will provide feedback as the contest goes on.

Target Market(s)

Hotel Concierges & Managers, Visitor Bureau Managers and Employees

Industry/Entity Type

Travel Industry

Font styles to use
Other font styles liked:
• Apple Fonts: San Francisco

Requirements
Must have
• We would like to use this library: https://quillarch.com/open-source/meridian/gallery
• The stats we would like to show are:
• (By day/month/time period)
• Number of Bookings
• Source of Bookings i.e. website vs mobile vs kiosk (% of a whole)
• Top 5 tour operators booked (and volume of each)
• Top 5 tours booked (and volume of each)
• Commissions earned (*admin only option - won't show for regular users)
Nice to have
• Would be nice to have an easy way for users to toggle between time periods that are common and also choose dates from drop down calendars.
• Will be used on an Slatebook and Slatebook Max

```html
<!DOCTYPE html>
<html lang="en">
<head>
<meta charset="utf-8">
<title>Slatebook Analytics Dashboard</title>
<link rel="stylesheet" href="https://fonts.googleapis.com/css2?family=Open+Sans:wght@400;600;700&display=swap">
<style>
:root{
  --backdrop:#3390b4;
  --sidebar:#3a3d42;
  --orange:#f26b12;
  --blue:#2f8db3;
  --green:#5fd0a2;
  --ink:#2b2b2b;
  --muted:#6b6b6b;
  --line:#e4e4e4;
  --panel:#ffffff;
  --canvas:#efefef;
}
*{box-sizing:border-box;margin:0;padding:0}
html,body{width:1200px;height:933px;overflow:hidden}
body{background:var(--backdrop);font-family:"Open Sans",Arial,sans-serif;color:var(--ink);position:relative}
.app{position:absolute;left:88px;top:98px;width:1024px;height:735px;background:var(--canvas);overflow:hidden}
.sidebar{position:absolute;left:0;top:0;width:40px;height:100%;background:var(--sidebar)}
.brand{position:absolute;left:0;top:10px;width:40px;text-align:center;font-size:7px;font-weight:700;color:var(--orange)}
.nav-active{position:absolute;left:0;top:44px;width:3px;height:30px;background:var(--orange)}
.nav-icon{position:absolute;left:12px;width:16px;height:16px}
.topbar{position:absolute;left:40px;top:0;right:0;height:36px;background:var(--panel);border-bottom:1px solid var(--line)}
.search-icon{position:absolute;left:30px;top:11px}
.search-label{position:absolute;left:52px;top:12px;font-size:9px;color:#555}
.date-range{position:absolute;left:762px;top:11px;height:19px;display:flex;border:1px solid var(--line);font-size:7px;color:#444}
.date-range .cal{width:22px;background:#f2f2f2;display:flex;align-items:center;justify-content:center}
.date-range .pick{padding:0 6px;display:flex;align-items:center;gap:3px;border-left:1px solid var(--line)}
.bell{position:absolute;left:950px;top:11px}
.more{position:absolute;left:970px;top:12px}
.sources{position:absolute;left:40px;top:36px;right:0;height:170px;background:var(--panel)}
.section-title{position:absolute;left:27px;top:12px;font-size:11px;color:#333;letter-spacing:.2px}
.filter{position:absolute;left:910px;top:16px}
.source-card{position:absolute;top:42px;width:286px;height:106px;background:var(--panel);box-shadow:0 1px 6px rgba(0,0,0,.12)}
.source-icon{position:absolute;left:40px;top:26px;width:28px;height:28px}
.source-name{position:absolute;left:0;width:108px;top:67px;text-align:center;font-size:8px;font-weight:700;letter-spacing:.3px}
.divider{position:absolute;left:128px;top:18px;width:1px;height:72px;background:var(--line)}
.gauge{position:absolute;left:155px;top:30px}
.percent{position:absolute;right:18px;top:38px;font-size:22px;color:#222}
.panel{position:absolute;background:var(--panel);box-shadow:0 1px 5px rgba(0,0,0,.12)}
.chart-panel{left:78px;top:228px;width:890px;height:227px}
.chart-panel svg{position:absolute;left:0;top:0}
.list-panel{top:483px;width:429px;height:228px}
.list-title{position:absolute;left:14px;top:14px;font-size:8px;font-weight:700;letter-spacing:.2px}
.list{list-style:none}
.list li{position:absolute;left:0;right:0;height:28px}
.avatar{position:absolute;left:14px;top:5px;width:17px;height:17px;border-radius:50%}
.item-name{position:absolute;left:51px;top:2px;font-size:11.5px;font-weight:600;color:#222;white-space:nowrap}
.item-sub{position:absolute;left:51px;top:16px;font-size:8px;color:#555;white-space:nowrap}
.scroll-track{position:absolute;left:422px;top:54px;width:3px;height:164px;background:#f0f0f0}
.scroll-thumb{position:absolute;left:0;top:0;width:3px;height:18px;background:#c8c8c8}
</style>
</head>
<body>
<main class="app">
  <aside class="sidebar">
    <div class="brand">Slatebook</div>
    <div class="nav-active"></div>
    <svg class="nav-icon" style="top:53px" viewBox="0 0 16 16"><rect x="3" y="4" width="10" height="9" fill="none" stroke="#f26b12" stroke-width="1.3"/><path d="M3 6.5h10M6 2.5v3M10 2.5v3M6 9.5l1.5 1.5 3-3" fill="none" stroke="#f26b12" stroke-width="1.2"/></svg>
    <svg class="nav-icon" style="top:110px" viewBox="0 0 16 16"><path d="M8 14 2.5 8.5A3 3 0 0 1 8 4.5a3 3 0 0 1 5.5 4Z" fill="#f26b12"/></svg>
    <svg class="nav-icon" style="top:167px" viewBox="0 0 16 16"><path d="M8 2l1.7 4 4.2.3-3.2 2.7 1 4.1L8 10.8 4.3 13.1l1-4.1L2.1 6.3l4.2-.3Z" fill="#f26b12"/></svg>
  </aside>

  <header class="topbar">
    <svg class="search-icon" width="14" height="14" viewBox="0 0 14 14"><circle cx="6" cy="6" r="4.5" fill="none" stroke="#666" stroke-width="1.1"/><path d="M9.3 9.3 13 13" stroke="#666" stroke-width="1.1"/></svg>
    <span class="search-label">Search</span>
    <div class="date-range">
      <div class="cal"><svg width="9" height="9" viewBox="0 0 9 9"><rect x="1" y="1.5" width="7" height="6.5" fill="none" stroke="#f26b12"/><path d="M1 3.5h7" stroke="#f26b12"/></svg></div>
      <div class="pick">MAY 29, 2017 <svg width="6" height="4" viewBox="0 0 6 4"><path d="M.5.5 3 3 5.5.5" fill="none" stroke="#333"/></svg></div>
      <div class="pick">JUN 20, 2017 <svg width="6" height="4" viewBox="0 0 6 4"><path d="M.5.5 3 3 5.5.5" fill="none" stroke="#333"/></svg></div>
    </div>
    <svg class="bell" width="14" height="14" viewBox="0 0 14 14"><path d="M3 10V6.5a3.5 3.5 0 0 1 7 0V10l1 1H2Z" fill="none" stroke="#666" stroke-width="1"/><circle cx="11" cy="11" r="2" fill="#f0413d"/></svg>
    <svg class="more" width="4" height="12" viewBox="0 0 4 12"><circle cx="2" cy="2" r="1.2" fill="#555"/><circle cx="2" cy="6" r="1.2" fill="#555"/><circle cx="2" cy="10" r="1.2" fill="#555"/></svg>
  </header>

  <section class="sources">
    <h2 class="section-title">SOURCE OF BOOKINGS</h2>
    <svg class="filter" width="16" height="14" viewBox="0 0 16 14"><path d="M0 2h16M0 7h16M0 12h16" stroke="#444" stroke-width="1.3"/><path d="M10 0v4M5 5v4M9 10v4" stroke="#444" stroke-width="1.3"/></svg>

    <article class="source-card" style="left:26px">
      <svg class="source-icon" viewBox="0 0 28 28"><circle cx="14" cy="14" r="12.5" fill="#f26b12"/><path d="M6 9c3 0 4 2 6 2s1 3 3 4-1 4-3 5c-1-2-3-2-3-5S6 12 6 9Zm10-5c2 2 1 4 3 5s4-1 5 2c-2 0-3 2-5 1s-3-3-3-8Z" fill="#fff"/></svg>
      <div class="source-name">WEBSITE</div>
      <div class="divider"></div>
      <svg class="gauge" width="50" height="50" viewBox="0 0 50 50"><circle cx="25" cy="25" r="22" fill="none" stroke="#eee" stroke-width="2.5"/><circle cx="25" cy="25" r="22" fill="none" stroke="#5fd0a2" stroke-width="2.5" stroke-dasharray="62 200" transform="rotate(92 25 25)"/><text x="13" y="28" font-size="7" fill="#5fd0a2">↓</text><text x="22" y="28" font-size="5" fill="#5fd0a2">12.2%</text></svg>
      <div class="percent">81%</div>
    </article>

    <article class="source-card" style="left:350px">
      <svg class="source-icon" viewBox="0 0 28 28"><rect x="8" y="1" width="12" height="25" rx="2" fill="#f26b12"/><rect x="10" y="4" width="8" height="17" fill="#fff"/><circle cx="14" cy="23.5" r="1" fill="#fff"/></svg>
      <div class="source-name">MOBILE</div>
      <div class="divider"></div>
      <svg class="gauge" width="50" height="50" viewBox="0 0 50 50"><circle cx="25" cy="25" r="22" fill="none" stroke="#eee" stroke-width="2.5"/><circle cx="25" cy="25" r="22" fill="none" stroke="#5fd0a2" stroke-width="2.5" stroke-dasharray="62 200" transform="rotate(92 25 25)"/><text x="13" y="28" font-size="7" fill="#5fd0a2">↓</text><text x="22" y="28" font-size="5" fill="#5fd0a2">10.9%</text></svg>
      <div class="percent">82%</div>
    </article>

    <article class="source-card" style="left:674px">
      <svg class="source-icon" viewBox="0 0 28 28"><path d="M4 3l5-1 3 6-3 2c1 3 4 6 7 7l2-3 6 3-1 5c-9 1-20-10-19-19Z" fill="#f26b12"/><path d="M15 6a7 7 0 0 1 7 7M15 2a11 11 0 0 1 11 11" fill="none" stroke="#f26b12" stroke-width="2.2"/></svg>
      <div class="source-name">KIOSK</div>
      <div class="divider"></div>
      <svg class="gauge" width="50" height="50" viewBox="0 0 50 50"><circle cx="25" cy="25" r="22" fill="none" stroke="#eee" stroke-width="2.5"/><circle cx="25" cy="25" r="22" fill="none" stroke="#5fd0a2" stroke-width="2.5" stroke-dasharray="62 200" transform="rotate(92 25 25)"/><text x="13" y="28" font-size="7" fill="#5fd0a2">↓</text><text x="24" y="28" font-size="5" fill="#5fd0a2">5.1%</text></svg>
      <div class="percent">61%</div>
    </article>
  </section>

  <section class="panel chart-panel">
    <svg width="890" height="227" viewBox="0 0 1113 284" font-family="Open Sans, Arial, sans-serif">
      <text x="17" y="24" font-size="10" font-weight="700" fill="#222">NEW BOOKINGS</text>
      <g font-size="10" fill="#333" text-anchor="end">
        <text x="35" y="57">250</text><text x="35" y="82">200</text><text x="35" y="107">150</text><text x="35" y="132">100</text><text x="35" y="157">0</text>
      </g>
      <line x1="53" y1="180" x2="508" y2="180" stroke="#e2e2e2"/>
      <g font-size="10" fill="#333" text-anchor="middle">
        <text x="74" y="205">29 JUN</text><text x="139" y="205">30 JUN</text><text x="201" y="205">01 JUL</text><text x="264" y="205">02 JUL</text><text x="327" y="205">03 JUL</text><text x="390" y="205">04 JUL</text><text x="453" y="205">05 JUL</text><text x="509" y="205">06 JUL</text>
      </g>
      <polyline points="60,146 130,118 192,150 252,130 318,153 387,89 453,148 504,117" fill="none" stroke="#f26b12" stroke-width="2.5" stroke-linejoin="round"/>
      <polyline points="60,140 130,108 192,156 252,121 318,140 387,98 453,141 509,132" fill="none" stroke="#2f8db3" stroke-width="2.5" stroke-linejoin="round"/>
      <circle cx="808" cy="21" r="4.5" fill="#2f8db3"/><text x="816" y="25" font-size="10.5" fill="#333">New bookings</text>
      <circle cx="945" cy="21" r="4.5" fill="#f26b12"/><text x="954" y="25" font-size="10.5" fill="#333">Booking extend</text>
      <circle cx="914" cy="142" r="93" fill="#2f8db3"/>
      <path d="M914 142 L981 79 A92 92 0 0 1 1006.5 153 Z" fill="#f26b12"/>
    </svg>
  </section>

  <section class="panel list-panel" style="left:78px">
    <h3 class="list-title">TOP 5 TOUR OPERATORS</h3>
    <ul class="list">
      <li style="top:40px"><span class="avatar" role="img" aria-label="Operator photo" style="background:#b5524a"></span><span class="item-name">AThirdCool Tour</span><span class="item-sub">AnotherCool Tour</span></li>
      <li style="top:78px"><span class="avatar" role="img" aria-label="Operator photo" style="background:#7f8f9c"></span><span class="item-name">Lakeside Bike Tours and Rentals</span><span class="item-sub">Lakeside-Music Bicycle Tour</span></li>
      <li style="top:116px"><span class="avatar" role="img" aria-label="Operator photo" style="background:#5e7a96"></span><span class="item-name">AThirdCool Tour</span><span class="item-sub">AnotherCool Tour</span></li>
      <li style="top:154px"><span class="avatar" role="img" aria-label="Operator photo" style="background:#6b4a3a"></span><span class="item-name">Lakeside Bike Tours and Rentals</span><span class="item-sub">Lakeside-Music Bicycle Tour</span></li>
      <li style="top:194px"><span class="avatar" role="img" aria-label="Operator photo" style="background:#8a7a5e"></span><span class="item-name">AThirdCool Tour</span><span class="item-sub">AnotherCool Tour</span></li>
    </ul>
    <div class="scroll-track"><div class="scroll-thumb"></div></div>
  </section>

  <section class="panel list-panel" style="left:539px">
    <h3 class="list-title">TOP 5 TOURS</h3>
    <ul class="list">
      <li style="top:40px"><span class="avatar" role="img" aria-label="Tour photo" style="background:#b5524a"></span><span class="item-name">AThirdCool Tour</span><span class="item-sub">AnotherCool Tour</span></li>
      <li style="top:78px"><span class="avatar" role="img" aria-label="Tour photo" style="background:#7f8f9c"></span><span class="item-name">Lakeside Bike Tours and Rentals</span><span class="item-sub">Lakeside-Music Bicycle Tour</span></li>
      <li style="top:116px"><span class="avatar" role="img" aria-label="Tour photo" style="background:#5e7a96"></span><span class="item-name">AThirdCool Tour</span><span class="item-sub">AnotherCool Tour</span></li>
      <li style="top:154px"><span class="avatar" role="img" aria-label="Tour photo" style="background:#6b4a3a"></span><span class="item-name">Lakeside Bike Tours and Rentals</span><span class="item-sub">Lakeside-Music Bicycle Tour</span></li>
      <li style="top:194px"><span class="avatar" role="img" aria-label="Tour photo" style="background:#8a7a5e"></span><span class="item-name">AThirdCool Tour</span><span class="item-sub">AnotherCool Tour</span></li>
    </ul>
    <div class="scroll-track"><div class="scroll-thumb"></div></div>
  </section>
</main>
</body>
</html>
```